Sales Page Header Design Project

Hi,
I need a background image created for this sales page: http://tidyventurecamp.example
Width: 977 px
Height: 150 px
Here are a few sample designs to work with: http://marketsummitschool.example/
http://crafthousepixel.example/wp-content/uploads/2011/02/experts1.png
Must be sharp, professional looking and uncluttered.
Colours: Must include blue (I like the blue on the on the current sales page, but will leave shade and colour combinations to your creativity)
Text = Tunde Marwick Presents
Tidy Venture Camp
Your Blueprint for Building a Profitable, Sustainable Business in Today's Economy!
Any questions, give me a shout
Entrepreneurs and Business Owners, aged 21 to 45
Business

```html
<!DOCTYPE html>
<html lang="en">
<head>
<meta charset="utf-8">
<title>Tidy Venture Camp – Header Concepts</title>
<link rel="stylesheet" href="https://fonts.googleapis.com/css2?family=Questrial&display=swap">
<style>
  :root {
    --page-bg: #ffffff;
    --city-silver-edge: #9c9c9c;
    --city-silver-core: #3a3a3a;
    --city-dark-edge: #6a6a6a;
    --city-dark-core: #2e2e2e;
    --city-peach-edge: #c99a84;
    --city-peach-core: #3b4048;
    --title-silver: #ececec;
    --title-grey: #a3a3a3;
    --title-peach: #e2ad92;
    --tagline-light: #e4e4e4;
    --tagline-peach: #dcc9c0;
    --extrude: rgba(0, 0, 0, 0.55);
  }
  * { box-sizing: border-box; margin: 0; padding: 0; }
  html, body {
    width: 1200px;
    height: 1000px;
    overflow: hidden;
    background: var(--page-bg);
  }
  .concept-sheet {
    position: relative;
    width: 1200px;
    height: 1000px;
    font-family: "Questrial", "Century Gothic", sans-serif;
  }
  .header-banner {
    position: absolute;
    left: 0;
    width: 1200px;
    height: 184px;
    overflow: hidden;
  }
  .header-banner--silver { top: 172px; }
  .header-banner--dark { top: 405px; }
  .header-banner--peach { top: 642px; }

  .cityscape {
    position: absolute;
    inset: 0;
  }
  .header-banner--silver .cityscape {
    background: radial-gradient(ellipse 60% 90% at 50% 50%, var(--city-silver-core) 0%, #474747 60%, var(--city-silver-edge) 100%);
  }
  .header-banner--dark .cityscape {
    background: radial-gradient(ellipse 60% 90% at 50% 50%, var(--city-dark-core) 0%, #3c3c3c 60%, var(--city-dark-edge) 100%);
  }
  .header-banner--peach .cityscape {
    background: radial-gradient(ellipse 60% 90% at 50% 50%, var(--city-peach-core) 0%, #4a4d55 60%, var(--city-peach-edge) 100%);
  }

  .banner-copy {
    position: absolute;
    inset: 0;
    text-align: center;
  }
  .banner-title {
    font-weight: 400;
    font-size: 74px;
    line-height: 66px;
    letter-spacing: 1px;
    padding-top: 22px;
    text-shadow:
      1px 1px 0 var(--extrude),
      2px 2px 0 var(--extrude),
      3px 3px 0 var(--extrude),
      6px 6px 10px rgba(0, 0, 0, 0.6);
  }
  .banner-title span { display: block; }
  .header-banner--silver .banner-title { color: var(--title-silver); }
  .header-banner--dark .banner-title { color: var(--title-grey); }
  .header-banner--peach .banner-title { color: var(--title-peach); }

  .banner-tagline {
    font-size: 20px;
    line-height: 24px;
    margin-top: 2px;
    text-shadow: 1px 1px 2px rgba(0, 0, 0, 0.7);
  }
  .header-banner--dark .banner-tagline { color: var(--tagline-light); }
  .header-banner--peach .banner-tagline { color: var(--tagline-peach); }
</style>
</head>
<body>
<main class="concept-sheet">

  <section class="header-banner header-banner--silver">
    <div class="cityscape" role="img" aria-label="3D render of a grey city skyline of block buildings seen from above"></div>
    <div class="banner-copy">
      <h1 class="banner-title"><span>Tunde Marwick Presents</span><span>Tidy Venture Camp</span></h1>
    </div>
  </section>

  <section class="header-banner header-banner--dark">
    <div class="cityscape" role="img" aria-label="3D render of a dark grey city skyline of block buildings seen from above"></div>
    <div class="banner-copy">
      <h1 class="banner-title"><span>Tunde Marwick Presents</span><span>Tidy Venture Camp</span></h1>
      <p class="banner-tagline">Your Blueprint for Building a Profitable, Sustainable Business in Today's Economy!</p>
    </div>
  </section>

  <section class="header-banner header-banner--peach">
    <div class="cityscape" role="img" aria-label="3D render of a slate blue city skyline with warm peach light at the edges"></div>
    <div class="banner-copy">
      <h1 class="banner-title"><span>Tunde Marwick Presents</span><span>Tidy Venture Camp</span></h1>
      <p class="banner-tagline">Your Blueprint for Building a Profitable, Sustainable Business in Today's Economy!</p>
    </div>
  </section>

</main>
</body>
</html>
```